Digital Menu Board for Restaurant

I want a digital menu board for our new restaurant. I have provided the sample of what I kind of want.
This is to be on a 55 inch tv so it needs to be the correct aspect ratio of 4:5

Font styles to use
Serif
Sans Serif

Colors
f59296
f04a50
ec1f27
ffffff
fffef7
fbed22
ffc214
0592cd
e5519f

Requirements
Must have
• fun, maybe something moving? bright colors on a darker background so it's easy to read or dark font on a light background.

```html
<!DOCTYPE html>
<html lang="en">
<head>
<meta charset="utf-8">
<title>Tide Hollow Menu Board</title>
<link rel="stylesheet" href="https://fonts.googleapis.com/css2?family=Michroma&family=Kaushan+Script&family=Yellowtail&family=Open+Sans:wght@400;600;700&display=swap">
<style>
  :root{
    --page:#ffffff;
    --board-dark:#1a0d07;
    --board-warm:#4a2412;
    --headline-green:#9bd63a;
    --section-orange:#f0552a;
    --item-blue:#1fa3dc;
    --desc-gold:#f7b52b;
    --drinks-green:#8cc63f;
    --sides-orange:#f15a29;
    --shakes-blue:#2aaae2;
    --ink:#1d1d1d;
    --white:#ffffff;
    --brand:#f26522;
  }
  *{margin:0;padding:0;box-sizing:border-box}
  html,body{width:1200px;height:960px;overflow:hidden;background:var(--page)}
  body{position:relative;font-family:"Open Sans",sans-serif}
  .board{position:absolute;left:24px;top:145px;width:1152px;height:670px;overflow:hidden}
  .board-photo{position:absolute;inset:0;
    background:radial-gradient(ellipse at 45% 60%, #6b3a1c 0%, var(--board-warm) 35%, var(--board-dark) 85%)}
  .combo-offers{position:absolute;left:39px;top:40px;font-family:"Michroma",sans-serif;
    color:var(--headline-green);font-size:24px;line-height:31px;letter-spacing:.5px;text-transform:uppercase;white-space:nowrap}
  .section-title{font-family:"Kaushan Script",cursive;color:var(--section-orange);font-size:31px;
    line-height:36px;margin:0 0 10px 16px;white-space:nowrap}
  .menu-column{position:absolute;top:196px;width:300px}
  .menu-column.buns{left:20px}
  .menu-column.green{left:338px}
  .item-name{display:block;width:max-content;min-width:150px;height:25px;padding:0 34px 0 16px;white-space:nowrap;
    background:linear-gradient(90deg,var(--item-blue) 0%,var(--item-blue) 60%,rgba(31,163,220,0) 100%);
    font-family:"Yellowtail",cursive;color:var(--white);font-size:17px;line-height:25px}
  .item-desc{padding:6px 0 2px 18px;color:var(--desc-gold);font-size:11.5px;line-height:15px;width:240px;min-height:53px}
  .green .item-desc{width:256px}
  .item-desc.short{min-height:40px}
  .kids{position:absolute;left:338px;top:527px;width:360px}
  .kids-title{height:44px;width:330px;padding-left:22px;white-space:nowrap;
    background:linear-gradient(90deg,var(--drinks-green) 0%,var(--drinks-green) 60%,rgba(140,198,63,.4) 100%);
    font-family:"Kaushan Script",cursive;color:var(--white);font-size:29px;line-height:44px;font-weight:700}
  .kids-list{padding:10px 0 0 23px;color:var(--white);font-size:15.5px;line-height:21.5px;white-space:nowrap}
  .brand{position:absolute;left:708px;top:92px;width:420px;display:flex;align-items:center;gap:14px}
  .brand-dot{width:44px;height:44px;border-radius:50%;background:var(--brand);flex:none}
  .brand-name{font-family:"Open Sans",sans-serif;font-weight:700;font-size:56px;line-height:1;color:var(--brand);white-space:nowrap}
  .info-box{position:absolute;left:724px;width:366px;border-radius:10px;text-align:center;color:var(--ink);white-space:nowrap}
  .info-box h2{font-family:"Kaushan Script",cursive;font-size:28px;line-height:32px;color:var(--ink)}
  .drinks{top:259px;height:87px;background:var(--drinks-green);padding-top:4px;font-size:14.5px;line-height:21px}
  .sides{top:357px;height:109px;background:var(--sides-orange);padding-top:6px;color:var(--white)}
  .sides ul{display:grid;grid-template-columns:180px 150px;list-style:none;text-align:left;
    padding-left:16px;font-size:15px;line-height:21px}
  .sides li::before{content:"\2022";color:var(--ink);margin-right:8px}
  .shakes{top:474px;height:172px;background:var(--shakes-blue);padding-top:3px;font-size:15px;line-height:20.8px}
</style>
</head>
<body>
<main class="board">
  <div class="board-photo" role="img" aria-label="Dim photo of a table full of barbecue dishes and drinks"></div>

  <div class="combo-offers">
    <p>Combp up!</p>
    <p>Add 1 side and drink</p>
    <p>Add 1 side and shake</p>
    <p>Additional sides</p>
  </div>

  <section class="menu-column buns">
    <h2 class="section-title">Between Buns</h2>
    <span class="item-name">1st Point Pulled Pork</span>
    <p class="item-desc">Pulled Pork, Rudy's Sassy BBQ Sauce, Chopped Bacon, Pepperjack Cheese, and Fried Jalapeno Peppers on a Ciabatta Bun</p>
    <span class="item-name">2nd Point Pulled Pork</span>
    <p class="item-desc short">Pulled Pork, Rudy's Sweet Respberry BBQ Sauce, and Coleslaw on a Ciabatta Bun</p>
    <span class="item-name">Spiniker Point Burger</span>
    <p class="item-desc">Smokehouse 1/2 Pound Burger, Crumbled Bacon, Rudy's Sassy BBQ Sauce, Cheese, and Onion Rings on a Toasted Brioche Bun</p>
    <span class="item-name">The Rock Burger</span>
    <p class="item-desc">Two Smokehouse 1/2 Pound Patties, Cheese, Lettuce, Tomato, Onion, Pickles, on Toasted Broiche Bun</p>
    <span class="item-name">Rainbow Cove Sandwich</span>
    <p class="item-desc">Chicken Salad - Smoked Chicken, Celery, and Onion Mixed with our BBQ Mayo and Topped with Seasoned Tomato on a Hoagie Roll.</p>
  </section>

  <section class="menu-column green">
    <h2 class="section-title">Green Shore</h2>
    <span class="item-name">North Beach Salad</span>
    <p class="item-desc">Pulled pord and Black Beans on a Bed of Romaine, Tomato and Onion with Sweet and Sour Respberry Pineapple Sauce.</p>
    <span class="item-name">West Side Salad</span>
    <p class="item-desc">BBQ Pulled Pork, Crumbled Bacon, Candied Walnuts, Fata Cheese, Red Onion, Spinach and Lettuce with Ranch Dressing or Raspberry Vinaigrette</p>
    <span class="item-name">Ease Side Salad</span>
    <p class="item-desc">Spinach and Lettuce, Chopped Apples, Candied Walnuts, Onion, Feta Cheese with Rudy's Respberry Vinaigrette<br>Add Chicken:</p>
  </section>

  <section class="kids">
    <h2 class="kids-title">Seashell Finders(Kids)</h2>
    <div class="kids-list">
      <p>Little Cheeseburger Pulled pork sandwich</p>
      <p>Mini Corn Dogs Chicken salad sandwich</p>
      <p>Fries/Onion Rings</p>
    </div>
  </section>

  <div class="brand">
    <span class="brand-dot"></span>
    <span class="brand-name">Tide Hollow</span>
  </div>

  <section class="info-box drinks">
    <h2>Drinks</h2>
    <p>Fizz Cola, Diet Fizz, Red Cola, Diet Red, Citrus Surge</p>
    <p>Diet Surge, Lemonade, Lemon-Lime, Dr Spice</p>
  </section>

  <section class="info-box sides">
    <h2>Sides</h2>
    <ul>
      <li>Seasoned Fries</li><li>Sweet Coleshlaw</li>
      <li>Onion Rings</li><li>Macaroni Salad</li>
      <li>Sweet Cornbread</li><li>Side Salad</li>
    </ul>
  </section>

  <section class="info-box shakes">
    <h2>Shakes</h2>
    <p>Rudy's Signature Raspberry Jammin Shake</p>
    <p>Raspberry Hazelnut Bobm Shake</p>
    <p>Raspberry Beachin' Shake (Pina Colada)</p>
    <p>Raspberry Browine Shake</p>
    <p>Caramel Shake</p>
    <p>Chocolate Shake</p>
  </section>
</main>
</body>
</html>
```